Psychology and personal development service needs an awesome Web Design

Hi, we are Bright, Steady & Kind, a psychology and personal development service located in Melbourne Australia. We already have a website www.brightsteady&kind.org but it is in great need of a makeover! We add to the website regularly with articles and so we need a space to archive these when they come off the main page, and we have products that we would like to sell internationally so we need a shop page that can convert currencies for international sales and calculate postage and handling. We have a plain square page that we would like to link as well as a newsletter that we would like to archive on the website. We have just had a logo designed through craft huddle and would like to incorporate this into our website. We want something with high visual impact and uncluttered.
We also run workshops and events so need a tab for this.
Thanks for getting on board!

```html
<!DOCTYPE html>
<html lang="en">
<head>
<meta charset="utf-8">
<title>Bright, Steady &amp; Kind</title>
<link rel="stylesheet" href="https://fonts.googleapis.com/css2?family=Zilla+Slab:wght@300;400&family=Source+Sans+3:ital,wght@0,400;0,600;1,400&display=swap">
<style>
:root{
  --teal:#2e9c8c;
  --teal-light:#7fd1c0;
  --purple:#b35aa6;
  --pink:#e79bc6;
  --blue:#2f9fd2;
  --ink:#333;
  --muted:#777;
  --rule:#cfcfcf;
  --footer:#2d2d2d;
  --footer-base:#232323;
  --footer-text:#bdbdbd;
  --field:#4a4a4a;
  --white:#fff;
}
*{box-sizing:border-box;margin:0;padding:0}
html,body{width:670px;height:1200px;overflow:hidden;background:var(--white)}
body{font-family:"Source Sans 3",Arial,sans-serif;color:var(--ink)}
.page{position:relative;width:670px;height:1200px;overflow:hidden}
.abs{position:absolute}

/* header */
.brand{left:78px;top:18px;display:flex;align-items:center;gap:6px}
.brand-dot{width:28px;height:28px;border-radius:50%;background:var(--purple)}
.brand-name{font-family:"Zilla Slab",serif;font-weight:400;font-size:13px;line-height:14px;color:var(--purple);width:70px}
.nav{right:78px;top:31px;display:flex;gap:22px;font-size:7px;text-transform:uppercase;color:#444}
.nav .active{color:var(--teal)}

/* hero */
.hero{left:0;top:70px;width:670px;height:254px;background:linear-gradient(100deg,#3fb3a0 0%,#8fd8c6 35%,#6cc6b1 60%,#3fa692 100%)}
.hero-photo{position:absolute;right:0;top:0;width:294px;height:254px;background:linear-gradient(90deg,rgba(120,200,170,0) 0%,#9fc9a8 20%,#5a4740 55%,#c9b2a4 80%,#e6e0da 100%)}
.hero-line{position:absolute;left:51px;height:24px;padding:0 13px;font-family:"Zilla Slab",serif;font-weight:300;font-size:13px;line-height:24px;color:var(--white);text-transform:uppercase;letter-spacing:.2px}
.l1{top:74px;width:257px;background:var(--purple)}
.l2{top:100px;width:290px;background:var(--teal)}
.l3{top:126px;width:257px;background:var(--pink)}
.l4{top:152px;width:175px;background:var(--blue)}
.dots{position:absolute;left:51px;top:228px;display:flex;gap:4px}
.dots span{width:7px;height:7px;border-radius:50%;background:var(--white)}
.dots .on{background:none;border:1px solid var(--white)}

/* section headings */
.section-title{font-family:"Zilla Slab",serif;font-weight:300;font-size:15px;color:#222}
.rule{height:0;border-top:1px dashed var(--rule)}
.frame{border:1px solid #ddd;padding:2px;background:var(--white)}
.frame div{width:100%;height:100%}

.tagline{left:79px;top:360px;font-size:7px;font-style:italic;color:var(--teal)}
.body-text{font-size:6.6px;line-height:13.6px;color:#666}
.welcome-text{left:205px;top:383px;width:387px;text-align:justify}

/* articles */
.article-title{font-size:7.4px;font-weight:600;color:var(--teal)}
.article-text{width:192px;font-size:6.4px;line-height:13.6px;color:#666;text-align:justify}
.meta{display:flex;gap:12px;font-size:6.2px;color:#999;align-items:center}
.meta span{display:flex;align-items:center;gap:3px}
.meta svg{width:6px;height:6px}

/* events */
.date{width:23px;height:25px;background:var(--teal);border-bottom:2px solid var(--purple);color:var(--white);font-size:6.6px;line-height:8px;text-align:center;padding-top:4px}
.event-title{font-size:7.4px;color:#333;text-transform:uppercase}
.event-text{width:150px;font-size:6.2px;line-height:12px;color:#666}

.btn{background:var(--teal);color:var(--white);font-size:6.6px;text-align:center;line-height:18px;height:18px;width:47px}

/* products */
.card{width:159px;height:181px;border:1px solid #ddd;background:var(--white)}
.card-img{position:absolute;left:7px;top:7px;width:143px;height:80px}
.card-title{position:absolute;left:10px;top:97px;font-size:7.2px;font-weight:600;color:var(--teal);text-transform:uppercase}
.card-text{position:absolute;left:10px;top:111px;width:140px;font-size:6.2px;line-height:11.5px;color:#888}
.pill{position:absolute;left:10px;top:150px;width:43px;height:17px;border-radius:9px;background:var(--teal);color:var(--white);font-size:6.2px;font-weight:600;text-align:center;line-height:17px}

/* footer */
.footer{left:0;top:1002px;width:670px;height:164px;background:var(--footer)}
.footer-base{left:0;top:1166px;width:670px;height:34px;background:var(--footer-base);border-top:1px solid #3a3a3a}
.copyright{width:670px;text-align:center;top:9px;font-size:6.6px;color:#aaa}
.foot-head{font-size:9px;color:var(--white);text-transform:uppercase}
.foot-text{font-size:6.6px;line-height:12px;color:var(--footer-text)}
.feed-item{display:flex;gap:6px;align-items:flex-start}
.feed-thumb{width:19px;height:19px;flex:none}
.field{width:99px;height:16px;background:var(--field);font-size:6.4px;color:#aaa;line-height:16px;padding-left:6px}
.subscribe{width:42px;height:15px;background:var(--teal);color:var(--white);font-size:6.4px;text-align:center;line-height:15px}
.social{display:flex;gap:6px}
.social span{width:18px;height:18px;border-radius:50%;background:var(--teal)}
</style>
</head>
<body>
<div class="page">

  <header>
    <div class="abs brand"><span class="brand-dot"></span><span class="brand-name">Bright, Steady &amp; Kind</span></div>
    <nav class="abs nav">
      <span class="active">Home</span><span>About Us</span><span>Services</span><span>Books</span><span>Online Store</span><span>Contact Us</span>
    </nav>
  </header>

  <section class="abs hero">
    <div class="hero-photo" role="img" aria-label="Photo of a stressed woman holding her temples"></div>
    <div class="hero-line l1">Focus only on what is important.</div>
    <div class="hero-line l2">Nourish your body, mind and spirit with</div>
    <div class="hero-line l3">good food, positive thoughts and</div>
    <div class="hero-line l4">affirmative actions.</div>
    <div class="dots"><span class="on"></span><span></span><span></span><span></span></div>
  </section>

  <section class="welcome">
    <h1 class="abs section-title" style="left:78px;top:340px">Welcome to Bright, Steady &amp; Kind</h1>
    <p class="abs tagline">We are a psychology and personal development Center</p>
    <div class="abs rule" style="left:78px;top:374px;width:514px"></div>
    <div class="abs frame" style="left:78px;top:387px;width:110px;height:80px">
      <div role="img" aria-label="Photo of a troubled businessman" style="background:linear-gradient(135deg,#dfe7ec,#8796a3 55%,#d7dfe4)"></div>
    </div>
    <p class="abs body-text welcome-text">Lorem ipsum dolor sit amet, consectetuer adipiscing elit. Aenean commodo ligula eget dolor. Aenean massa. Cum sociis natoque penatibus et magnis dis parturient montes, nascetur ridiculus mus. Donec quam felis, ultricies nec, pellentesque eu, pretium quis, sem. Nulla consequat massa quis enim. Donec pede justo, fringilla vel, aliquet nec, vulputate eget, arcu. In enim justo, rhoncus ut, imperdiet a, venenatis vitae, Lorem ipsum dolor sit amet, consectetuer adipiscing elit. Aenean commodo ligula eget dolor. Aenean massa. Cum sociis natoque penatibus et magnis dis parturient montes, nascetur ridiculus mus. Donec quam felis, ultricies nec, pellentesque eu, pretium quis, sem. Nulla consequat massa quis enim.</p>
  </section>

  <section class="articles">
    <h2 class="abs section-title" style="left:78px;top:493px">Latest Articles</h2>
    <div class="abs rule" style="left:78px;top:517px;width:280px"></div>

    <div class="abs frame" style="left:78px;top:534px;width:72px;height:71px">
      <div role="img" aria-label="Photo of a tired woman at a desk" style="background:linear-gradient(135deg,#e6e6e6,#8a7a70 60%,#d8d8d8)"></div>
    </div>
    <p class="abs article-title" style="left:166px;top:535px">Lorem ipsum dolor sit amet, consectetuer adipiscing elit</p>
    <p class="abs article-text" style="left:165px;top:547px">Lorem ipsum dolor sit amet, consectetuer adipiscing elit. Aenean commodo ligula eget dolor. Aenean massa. Cum sociis natoque penatibus et magnis dis parturient montes.</p>
    <div class="abs rule" style="left:164px;top:594px;width:194px"></div>
    <div class="abs meta" style="left:170px;top:599px">
      <span><svg viewBox="0 0 6 6"><rect x=".5" y="1" width="5" height="4.5" fill="none" stroke="#aaa" stroke-width=".8"/></svg>June 12,2014</span>
      <span><svg viewBox="0 0 6 6"><path d="M.5 1h5v3H2L1 5.5V4H.5z" fill="#aaa"/></svg>2 Comments</span>
      <span><svg viewBox="0 0 6 6"><path d="M.5.5h3l2 2.5-2.5 2.5-2.5-2.5z" fill="#aaa"/></svg>Admin</span>
      <span style="margin-left:14px"><svg viewBox="0 0 6 6"><path d="M3 5.5L.6 3A1.3 1.3 0 013 1.3 1.3 1.3 0 015.4 3z" fill="#aaa"/></svg>253</span>
    </div>

    <div class="abs frame" style="left:78px;top:625px;width:72px;height:71px">
      <div role="img" aria-label="Photo of a worried woman holding her head" style="background:linear-gradient(135deg,#e9e9e9,#b8a596 55%,#5b4a42 80%,#e0e0e0)"></div>
    </div>
    <p class="abs article-title" style="left:166px;top:626px">Lorem ipsum dolor sit amet, consectetuer adipiscing elit</p>
    <p class="abs article-text" style="left:165px;top:638px">Lorem ipsum dolor sit amet, consectetuer adipiscing elit. Aenean commodo ligula eget dolor. Aenean massa. Cum sociis natoque penatibus et magnis dis parturient montes.</p>
    <div class="abs rule" style="left:164px;top:685px;width:194px"></div>
    <div class="abs meta" style="left:170px;top:690px">
      <span><svg viewBox="0 0 6 6"><rect x=".5" y="1" width="5" height="4.5" fill="none" stroke="#aaa" stroke-width=".8"/></svg>June 12,2014</span>
      <span><svg viewBox="0 0 6 6"><path d="M.5 1h5v3H2L1 5.5V4H.5z" fill="#aaa"/></svg>2 Comments</span>
      <span><svg viewBox="0 0 6 6"><path d="M.5.5h3l2 2.5-2.5 2.5-2.5-2.5z" fill="#aaa"/></svg>Admin</span>
      <span style="margin-left:14px"><svg viewBox="0 0 6 6"><path d="M3 5.5L.6 3A1.3 1.3 0 013 1.3 1.3 1.3 0 015.4 3z" fill="#aaa"/></svg>253</span>
    </div>

    <div class="abs btn" style="left:78px;top:711px">View All</div>
  </section>

  <section class="events">
    <h2 class="abs section-title" style="left:403px;top:493px">Workshop / Events</h2>
    <div class="abs rule" style="left:403px;top:517px;width:189px"></div>

    <div class="abs date" style="left:404px;top:533px">15<br>OCT</div>
    <p class="abs event-title" style="left:441px;top:533px">Aenean commodo ligula eget dolor.</p>
    <p class="abs event-text" style="left:440px;top:547px">Donec viverra auctor lobortis. Pellentesque eu est a nulla placerat dignissim. Morbi a enim</p>
    <div class="abs rule" style="left:403px;top:578px;width:189px;border-top-style:solid;border-color:#e2e2e2"></div>

    <div class="abs date" style="left:404px;top:590px">12<br>OCT</div>
    <p class="abs event-title" style="left:441px;top:590px">Aenean commodo ligula eget dolor.</p>
    <p class="abs event-text" style="left:440px;top:604px">Donec viverra auctor lobortis. Pellentesque eu est a nulla placerat dignissim. Morbi a enim</p>
    <div class="abs rule" style="left:403px;top:640px;width:189px;border-top-style:solid;border-color:#e2e2e2"></div>

    <div class="abs date" style="left:404px;top:647px">9<br>OCT</div>
    <p class="abs event-title" style="left:441px;top:647px">Aenean commodo ligula eget dolor.</p>
    <p class="abs event-text" style="left:440px;top:663px">Donec viverra auctor lobortis. Pellentesque eu est a nulla placerat dignissim. Morbi a enim</p>

    <div class="abs btn" style="left:403px;top:711px">View All</div>
  </section>

  <section class="products">
    <h2 class="abs section-title" style="left:78px;top:748px">Our Products</h2>
    <div class="abs rule" style="left:78px;top:773px;width:514px"></div>

    <article class="abs card" style="left:78px;top:791px">
      <div class="card-img" role="img" aria-label="Book cover with a dark portrait photo" style="background:linear-gradient(90deg,#2a2522,#4a3d36 60%,#7a6658)"></div>
      <h3 class="card-title">Ruth - A Quiet Beginning</h3>
      <p class="card-text">Seventeen-year-old Ruth is on a search for identity and transformation as she attempts to come to terms with the death of her mother.</p>
      <span class="pill">More Info</span>
    </article>

    <article class="abs card" style="left:256px;top:791px">
      <div class="card-img" role="img" aria-label="Book cover with a sepia photo of a clock tower" style="background:linear-gradient(135deg,#d8c8a8,#9b8563 50%,#5e4f3c)"></div>
      <h3 class="card-title">Steadfast</h3>
      <p class="card-text">Seventeen-year-old Ruth is on a search for identity and transformation as she attempts to come to terms with the death of her mother.</p>
      <span class="pill">More Info</span>
    </article>

    <article class="abs card" style="left:434px;top:791px">
      <div class="card-img" role="img" aria-label="Product photo of an audio disc box set" style="background:linear-gradient(135deg,#e2e2e2,#3c4f9a 50%,#d9d9d9)"></div>
      <h3 class="card-title">A Small Book of Calm</h3>
      <p class="card-text">Seventeen-year-old Ruth is on a search for identity and transformation as she attempts to come to terms with the death of her mother.</p>
      <span class="pill">More Info</span>
    </article>
  </section>

  <footer>
    <div class="abs footer">
      <div class="abs" style="left:83px;top:18px;width:150px">
        <h4 class="foot-head">Social Network Feeds</h4>
        <div class="feed-item" style="margin-top:12px">
          <span class="feed-thumb" style="width:15px;height:15px;background:#3f5a96"></span>
          <div class="foot-text" style="line-height:9px"><span style="color:#ddd">Bright, Steady &amp; Kind</span><br><i style="font-size:5.6px">October 21 at 12:32pm</i></div>
        </div>
        <div class="feed-item" style="margin-top:7px">
          <span class="feed-thumb" role="img" aria-label="Small profile photo" style="background:linear-gradient(135deg,#c9a58a,#e8d8c8)"></span>
          <p class="foot-text" style="line-height:10.5px">"I received a $28,000 college scholarship, which made this class</p>
        </div>
        <div class="feed-item" style="margin-top:12px">
          <span class="feed-thumb" role="img" aria-label="Small profile photo" style="background:linear-gradient(135deg,#d8c0b0,#f0ebe8)"></span>
          <p class="foot-text" style="line-height:10.5px">"I received a $28,000 college scholarship, which made this class</p>
        </div>
        <div class="feed-item" style="margin-top:7px">
          <span class="feed-thumb" role="img" aria-label="Small profile photo" style="background:linear-gradient(135deg,#b8c6d4,#eef1f4)"></span>
          <p class="foot-text" style="line-height:10.5px">"I received a $28,000 college scholarship, which made this class</p>
        </div>
      </div>

      <div class="abs" style="left:247px;top:18px;width:120px">
        <h4 class="foot-head">Contact</h4>
        <p class="foot-text" style="margin-top:14px">Single ZIP city, unique first letter of single street name: 42 Willow Bend Rd. Fairhaven VT 05743</p>
        <p class="foot-text" style="margin-top:6px;font-size:7.2px">Give us a Call</p>
        <div style="display:flex;gap:8px;margin-top:6px;align-items:center">
          <svg width="10" height="17" viewBox="0 0 10 17"><rect x="1" y="1" width="8" height="15" rx="1.5" fill="none" stroke="var(--teal)" stroke-width="1.4"/><line x1="4" y1="13.5" x2="6" y2="13.5" stroke="var(--teal)" stroke-width="1.2"/></svg>
          <p class="foot-text" style="line-height:11px">+1 (555) 010 42 42<br>+1 (555) 014 377 18</p>
        </div>
      </div>

      <div class="abs" style="left:376px;top:18px">
        <h4 class="foot-head">Weekly Newsletter</h4>
        <div class="field" style="margin-top:12px">Name</div>
        <div class="field" style="margin-top:14px">Email</div>
        <div class="subscribe" style="margin-top:15px">Subscribe</div>
      </div>

      <div class="abs" style="left:499px;top:18px">
        <h4 class="foot-head">Our Products</h4>
        <p class="foot-text" style="margin-top:12px;line-height:11.5px">Product 1<br>Product 2<br>Product 2</p>
        <p class="foot-text" style="margin-top:8px;font-size:7.2px">Social Networks</p>
        <div class="social" style="margin-top:7px"><span></span><span></span><span></span><span></span></div>
      </div>
    </div>
    <div class="abs footer-base">
      <p class="abs copyright">© Copyright 2014 . www.brightsteady&amp;kind.org.  All rights reserved.</p>
    </div>
  </footer>

</div>
</body>
</html>
```